Biz Card for Harrowfield Property Partners - HWPP

Harrowfield Property Partners is a commercial real estate acquisitions firm. We buy commercial property and need to raise capital from investors for each deal we buy. The vibe needs to be: give us your money, we will multiply it.
Our website: www.hrwpp-example.com
Competitors are: https://velmarholdings-example.com/, https://tribanquepartners-example.com/, http://www.ostrellecapital-example.com/
Target Market(s)
High Net Worth Individuals, Bankers, Insurance Companies, Commercial Real Estate Brokers.
Industry/Entity Type
Investment Banking
Contact Information for Business Card
Name, Title, Addess, Cell#, Office#, email, website
Requirements
Must have
- use one of our logos. See website for look and feel: www.hrwpp-example.com
Nice to have
- see website: www.hrwpp-example.com

```html
<!DOCTYPE html>
<html lang="en">
<head>
<meta charset="utf-8">
<title>Harrowfield Property Partners – Business Card</title>
<link href="https://fonts.googleapis.com/css2?family=Josefin+Sans:wght@300;400;600&display=swap" rel="stylesheet">
<style>
  :root {
    --navy: #00223b;
    --paper: #efefef;
    --backdrop: #e6e6e6;
    --muted: #6f747a;
    --rule: #8a8a8a;
    --white: #f2f2f2;
  }
  * { margin: 0; padding: 0; box-sizing: border-box; }
  html, body { width: 1200px; height: 1200px; overflow: hidden; }
  body {
    background: var(--backdrop);
    font-family: "Josefin Sans", sans-serif;
    position: relative;
  }
  .card {
    position: absolute;
    left: 227px;
    width: 745px;
    height: 425px;
    border-radius: 38px;
    overflow: hidden;
  }
  .card--front { top: 135px; background: var(--paper); color: var(--navy); }
  .card--back { top: 638px; background: var(--navy); color: var(--white); }

  /* brand lockup */
  .brand-dot { position: absolute; border-radius: 50%; }
  .card--front .brand-dot { left: 33px; top: 33px; width: 106px; height: 106px; background: var(--navy); }
  .card--back .brand-dot { left: 309px; top: 91px; width: 140px; height: 140px; background: var(--white); }
  .brand-name {
    position: absolute;
    font-weight: 400;
    text-transform: uppercase;
    letter-spacing: 0.2em;
    line-height: 1.35;
  }
  .card--front .brand-name { left: 160px; top: 55px; font-size: 25px; color: var(--navy); }
  .card--back .brand-name { left: 0; right: 0; top: 262px; font-size: 30px; text-align: center; color: var(--white); padding-left: 0.2em; }

  /* person */
  .person { position: absolute; left: 34px; top: 218px; }
  .person__name { font-size: 29px; font-weight: 600; letter-spacing: 0.02em; line-height: 1.1; }
  .person__title { font-size: 18px; font-weight: 300; color: var(--muted); margin-top: 4px; }

  .divider { position: absolute; left: 0; right: 0; top: 292px; height: 1px; background: var(--rule); }
  .divider__accent { position: absolute; left: 34px; top: -1px; width: 228px; height: 3px; background: var(--navy); }

  /* contacts */
  .contacts { position: absolute; left: 33px; top: 320px; list-style: none; }
  .contacts li { display: flex; align-items: center; height: 25.5px; font-size: 18px; font-weight: 300; color: var(--muted); }
  .contacts svg { width: 18px; height: 18px; margin-right: 11px; flex: none; }
  .contacts strong { color: var(--navy); font-weight: 600; }

  .address {
    position: absolute; right: 33px; top: 345px;
    text-align: right; font-size: 18px; font-weight: 300; color: var(--muted); line-height: 25.5px;
  }
</style>
</head>
<body>

<section class="card card--front" aria-label="Business card front">
  <span class="brand-dot" aria-hidden="true"></span>
  <div class="brand-name">Harrowfield<br>Property Partners</div>

  <div class="person">
    <div class="person__name">DANIEL R. WHITCOMBE</div>
    <div class="person__title">Director of Finance</div>
  </div>

  <div class="divider"><span class="divider__accent"></span></div>

  <ul class="contacts">
    <li>
      <svg viewBox="0 0 18 18" aria-hidden="true"><circle cx="9" cy="9" r="9" fill="#00223b"/><path d="M4.5 7.5c0-1.5 2-2.5 4.5-2.5s4.5 1 4.5 2.5l-1.5.5-.6-1.3c-1.5-.5-3.3-.5-4.8 0L6 8z" fill="#efefef"/><rect x="5.5" y="8.5" width="7" height="4.5" rx="1" fill="#efefef"/><circle cx="9" cy="10.7" r="1.2" fill="#00223b"/></svg>
      (555) 014-2290
    </li>
    <li>
      <svg viewBox="0 0 18 18" aria-hidden="true"><circle cx="9" cy="9" r="9" fill="#00223b"/><rect x="4.5" y="5.8" width="9" height="6.4" fill="none" stroke="#efefef" stroke-width="1.1"/><path d="M4.5 5.8 9 9.6l4.5-3.8" fill="none" stroke="#efefef" stroke-width="1.1"/></svg>
      info@hrwpp-example.com
    </li>
    <li>
      <svg viewBox="0 0 18 18" aria-hidden="true"><circle cx="9" cy="9" r="9" fill="#00223b"/><circle cx="9" cy="9" r="5" fill="none" stroke="#efefef" stroke-width="1.1"/><path d="M4 9h10M9 4c-2 3-2 7 0 10M9 4c2 3 2 7 0 10" fill="none" stroke="#efefef" stroke-width="1"/></svg>
      <span>www.<strong>hrwpp-example</strong>.com</span>
    </li>
  </ul>

  <div class="address">480 Calloway Ave, Suite 1410<br>Marston Bay, FL 30912</div>
</section>

<section class="card card--back" aria-label="Business card back">
  <span class="brand-dot" aria-hidden="true"></span>
  <div class="brand-name">Harrowfield<br>Property Partners</div>
</section>

</body>
</html>
```